In Home Senior Care Agency Business Card Design Needed

At Silver Birch Helpers, we don't just work in the care-giving industry. We truly care.

We are dedicated to providing personable, hands-on and integrated caring services that aim to help people maintain safe and comfortable life standards within the familiar settings of their own homes.

We would like to see designs that use my logo colors obviously. The final design will be modern, yet professional and semi-minimalistic. It should communicate an well-established company that is innovative. We would also like the design to have that 'flat' design look. Ideally having the design roll over to the backend of the card. Most likely it will be printed on a Matte paper with a die cut (either 2 rounded corners -leaf cut) or all rounded.

Target Market(s)

Baby boomer generation. 45 years and older.

Industry/Entity Type

Business

Contact Information for Business Card

Text for Front:
Slogan somewhere "Our Family. Caring For Yours.”

Darren Holloway
President

Cell: 512.608.7719
Phone: 512.274.6051
E: Darren@silverbirchhelpers.net
W: www.SilverBirchHelpers.net

Back:
-Meal Preparation
-Transportation
-Light Housekeeping
-Bathing Assistance
-Companionship

Font styles to use
Serif
Sans Serif

Requirements
Must have
• Flat, modern, professional design. Not too many colors. Match my colors in logo. Design of card must reflect from the front onto the back. Evenly spaced font.
Nice to have
• Try to work off current logo scheme, but logo may need to be redesigned.
Should not have
• Not too many colors.

```html
<!DOCTYPE html>
<html lang="en">
<head>
<meta charset="utf-8">
<title>Silver Birch Helpers – Business Card</title>
<link rel="stylesheet" href="https://fonts.googleapis.com/css2?family=Exo+2:wght@400;600&display=swap">
<style>
  :root {
    --page-bg: #e9e7e3;
    --card-bg: #ffffff;
    --card-shade: #f1f1f1;
    --accent-orange: #f2a93b;
    --accent-olive: #8b7b3c;
    --brand-green: #1f6a3a;
    --text-dark: #3a3a3a;
    --text-mid: #5a5a5a;
  }
  * { margin: 0; padding: 0; box-sizing: border-box; }
  html, body {
    width: 1200px; height: 900px; overflow: hidden;
    background: var(--page-bg);
    font-family: "Exo 2", sans-serif;
  }
  .sheet {
    width: 1200px; height: 900px;
    display: flex; align-items: center; justify-content: center; gap: 40px;
  }
  .card {
    position: relative;
    width: 520px; height: 297px;
    border-radius: 28px;
    background: radial-gradient(ellipse at 50% 40%, var(--card-bg) 55%, var(--card-shade) 100%);
    box-shadow: 0 2px 10px rgba(0,0,0,0.12);
    overflow: hidden;
  }

  /* Front */
  .identity {
    position: absolute; left: 34px; top: 28px;
    display: flex; align-items: center; gap: 14px;
  }
  .identity-icon { width: 34px; height: 34px; flex: none; }
  .person-name {
    font-weight: 600; font-size: 17px; letter-spacing: 1px;
    color: var(--text-dark); text-transform: uppercase;
  }
  .person-title {
    font-size: 14px; letter-spacing: 1.5px; color: var(--text-mid);
    margin-top: 2px;
  }
  .divider {
    position: absolute; left: 82px; right: 40px; top: 90px;
    height: 3px; background: var(--accent-orange);
  }
  .contacts {
    position: absolute; left: 34px; top: 112px;
    list-style: none;
    display: flex; flex-direction: column; gap: 10px;
  }
  .contact-row { display: flex; align-items: center; gap: 14px; }
  .contact-icon { width: 26px; height: 26px; flex: none; }
  .contact-text {
    font-size: 12px; line-height: 15px; letter-spacing: 0.6px;
    color: var(--text-mid);
  }
  .brand {
    position: absolute; right: 34px; bottom: 30px;
    display: flex; flex-direction: column; align-items: flex-end; gap: 4px;
  }
  .brand-row { display: flex; align-items: center; gap: 9px; }
  .brand-mark {
    width: 14px; height: 14px; border-radius: 50%;
    background: var(--brand-green);
  }
  .brand-name {
    font-weight: 600; font-size: 19px; color: var(--brand-green);
    letter-spacing: 0.4px;
  }
  .slogan {
    font-size: 12px; letter-spacing: 0.8px; color: var(--accent-olive);
  }

  /* Back */
  .services {
    position: absolute; left: 0; right: 0; top: 50%;
    transform: translateY(-50%);
    list-style: none; text-align: center;
    font-size: 19px; line-height: 27px; letter-spacing: 1.5px;
    color: var(--text-mid);
  }
</style>
</head>
<body>
<main class="sheet">

  <section class="card card-front" aria-label="Business card front">
    <div class="identity">
      <svg class="identity-icon" viewBox="0 0 34 34" aria-hidden="true">
        <circle cx="17" cy="17" r="17" fill="var(--accent-orange)"/>
        <circle cx="17" cy="13" r="5" fill="#fff"/>
        <path d="M8 26c1.5-5 5-7 9-7s7.5 2 9 7z" fill="#fff"/>
      </svg>
      <div>
        <p class="person-name">Darren Holloway</p>
        <p class="person-title">President</p>
      </div>
    </div>
    <div class="divider"></div>

    <ul class="contacts">
      <li class="contact-row">
        <svg class="contact-icon" viewBox="0 0 26 26" aria-hidden="true">
          <circle cx="13" cy="13" r="13" fill="var(--accent-olive)"/>
          <rect x="8.5" y="6.5" width="9" height="13" rx="1.5" fill="none" stroke="#fff" stroke-width="1.6"/>
          <circle cx="13" cy="17" r="0.9" fill="#fff"/>
        </svg>
        <p class="contact-text">Cell: 512.608.7719<br>Phone: 512.274.6051</p>
      </li>
      <li class="contact-row">
        <svg class="contact-icon" viewBox="0 0 26 26" aria-hidden="true">
          <circle cx="13" cy="13" r="13" fill="var(--accent-olive)"/>
          <rect x="7" y="8" width="12" height="10" rx="1.5" fill="none" stroke="#fff" stroke-width="1.6"/>
        </svg>
        <p class="contact-text">Darren@silverbirchhelpers.net<br>www.SilverBirchHelpers.net</p>
      </li>
      <li class="contact-row">
        <svg class="contact-icon" viewBox="0 0 26 26" aria-hidden="true">
          <circle cx="13" cy="13" r="13" fill="var(--accent-olive)"/>
          <path d="M13 20s-5-5.2-5-8.6a5 5 0 0 1 10 0C18 14.8 13 20 13 20z" fill="#fff"/>
          <circle cx="13" cy="11.4" r="1.8" fill="var(--accent-olive)"/>
        </svg>
        <p class="contact-text">214 Maple Ridge Road, Suite 6<br>Austin TX</p>
      </li>
    </ul>

    <div class="brand">
      <div class="brand-row">
        <span class="brand-mark" aria-hidden="true"></span>
        <span class="brand-name">Silver Birch Helpers</span>
      </div>
      <p class="slogan">Our Family. Caring For Yours.</p>
    </div>
  </section>

  <section class="card card-back" aria-label="Business card back">
    <ul class="services">
      <li>-Meal Preparation -</li>
      <li>Transportation -</li>
      <li>Light Housekeeping -</li>
      <li>Bathing Assistance -</li>
      <li>Companionship</li>
    </ul>
  </section>

</main>
</body>
</html>
```